Oil Field Service company needs professional business cards

Looking to clean up our current company business cards and look a little more professional. Harlow Tubular Services is a US based company that services the oil field. We deal with engineers, managers and oil rigs....................................................................................................................................................................................................................................................................................................................................................................................................

Target Market(s)

Oil and Gas professionals

Industry/Entity Type

Oil And Gas

Contact Information for Business Card

See attached photo as example

Font styles to use
Sans Serif

Colors
ec1f27

Requirements
Must have
• Company Logo, Name, Title, Cell, Office, Fax, Email.
• See attached photo
Nice to have
• External CRT, Internal CRT, Casing Crews, Torque Turn, Laydown Machine
Should not have
• Do not introduce any new pictures and keep it professional looking

```html
<!DOCTYPE html>
<html lang="en">
<head>
<meta charset="utf-8">
<title>Harlow Tubular Services – Business Card</title>
<link href="https://fonts.googleapis.com/css2?family=Lato:wght@400;700;900&display=swap" rel="stylesheet">
<style>
  :root {
    --slate: #3a4f5d;
    --red: #ec1f27;
    --paper: #ffffff;
    --backdrop: #e3e5e7;
    --ink-light: #ffffff;
  }
  * { box-sizing: border-box; margin: 0; padding: 0; }
  html, body { width: 1200px; height: 900px; overflow: hidden; }
  body {
    background: var(--backdrop);
    font-family: "Lato", Arial, sans-serif;
    position: relative;
  }
  .card {
    position: absolute;
    left: 280px;
    width: 640px;
    height: 366px;
    background: var(--paper);
    box-shadow: 0 6px 18px rgba(0,0,0,.18);
    overflow: hidden;
  }
  .card--front { top: 48px; }
  .card--back { top: 470px; display: flex; }

  .brand {
    display: flex;
    align-items: center;
    gap: 14px;
    color: var(--slate);
    font-weight: 900;
  }
  .brand__dot {
    width: 22px; height: 22px;
    border-radius: 50%;
    background: var(--red);
    flex: none;
  }
  .brand__name { line-height: 1; text-transform: uppercase; }
  .brand__name .line-main { display: block; font-size: 54px; letter-spacing: 1px; }
  .brand__name .line-sub { display: block; font-size: 15px; letter-spacing: 5px; margin-top: 8px; }

  .card--front .brand { position: absolute; left: 50%; top: 50%; transform: translate(-50%, -50%); }

  .back__brand-side {
    width: 45%;
    display: flex;
    align-items: flex-start;
    justify-content: center;
    padding-top: 140px;
  }
  .back__brand-side .brand__name .line-main { font-size: 38px; }
  .back__brand-side .brand__name .line-sub { font-size: 11px; letter-spacing: 3px; margin-top: 6px; }
  .back__brand-side .brand { gap: 10px; }
  .back__brand-side .brand__dot { width: 16px; height: 16px; }

  .back__panel {
    width: 55%;
    background: var(--slate);
    color: var(--ink-light);
    padding: 40px 34px 30px 20px;
    display: flex;
    flex-direction: column;
    justify-content: space-between;
    text-align: right;
  }
  .person__name { font-size: 22px; font-weight: 700; letter-spacing: .3px; }
  .person__title { font-size: 15px; color: var(--red); margin-top: 2px; }

  .contact { list-style: none; }
  .contact__item {
    display: flex;
    justify-content: flex-end;
    align-items: center;
    gap: 12px;
    font-size: 15px;
    line-height: 25px;
  }
  .contact__icon { width: 14px; height: 14px; fill: var(--ink-light); flex: none; }
</style>
</head>
<body>

  <section class="card card--front" aria-label="Card front">
    <div class="brand">
      <span class="brand__dot"></span>
      <span class="brand__name"><span class="line-main">Harlow</span><span class="line-sub">Tubular Services</span></span>
    </div>
  </section>

  <section class="card card--back" aria-label="Card back">
    <div class="back__brand-side">
      <div class="brand">
        <span class="brand__dot"></span>
        <span class="brand__name"><span class="line-main">Harlow</span><span class="line-sub">Tubular Services</span></span>
      </div>
    </div>
    <div class="back__panel">
      <div class="person">
        <p class="person__name">Cody Whitfield</p>
        <p class="person__title">Area Manager</p>
      </div>
      <ul class="contact">
        <li class="contact__item">(555) 214-8123
          <svg class="contact__icon" viewBox="0 0 16 16" aria-label="Office"><path d="M3.5 1l2.5 3-1.5 1.6c.8 1.9 2.2 3.3 4.1 4.1L10.2 8.2 13.5 10.5 12.3 13.8C6.6 13.5 2.4 9.3 2 3.6z"/></svg>
        </li>
        <li class="contact__item">(555) 318-6042
          <svg class="contact__icon" viewBox="0 0 16 16" aria-label="Cell"><path d="M4.5 1h7a1 1 0 011 1v12a1 1 0 01-1 1h-7a1 1 0 01-1-1V2a1 1 0 011-1zm.5 2v9h6V3zm3 10a.8.8 0 100 1.6.8.8 0 000-1.6z"/></svg>
        </li>
        <li class="contact__item">(555) 214-9317
          <svg class="contact__icon" viewBox="0 0 16 16" aria-label="Fax"><path d="M4 1h6l2 2v3H4zM2 7h12a1 1 0 011 1v5h-2v2H3v-2H1V8a1 1 0 011-1zm3 4v3h6v-3z"/></svg>
        </li>
        <li class="contact__item">codywhitfield@harlowtubular.com
          <svg class="contact__icon" viewBox="0 0 16 16" aria-label="Email"><path d="M1 3h14v10H1zm1.5 1.2L8 8.6l5.5-4.4z"/></svg>
        </li>
        <li class="contact__item">Redfield, OK 73099
          <svg class="contact__icon" viewBox="0 0 16 16" aria-label="Address"><path d="M8 1a5 5 0 015 5c0 3.5-5 9-5 9S3 9.5 3 6a5 5 0 015-5zm0 3a2 2 0 100 4 2 2 0 000-4z"/></svg>
        </li>
      </ul>
    </div>
  </section>

</body>
</html>
```